依頼詳細
PCとスマホデザインの両方納品をいただきますが、
まずはデザインイメージが確認しやすいPCページのみの提案をお願いします。
スマホページは当選者に納品時にお願いしたいと思います。
スマホサイズは横幅750pxのサイズで作成してください。

レスポンシブウェブデザインを意識したデザインでお願いします。

デザインに関しては、添付してあるデザインレイアウト設計シートを基にお願いします。
参考サイトのURLはデザインレイアウト設計シートに記載してあります。

画像データについては、既存サイトや参考サイト、フリー素材から流用してイメージ画像に当て込んでください。
足りない場合は、一旦他のサイトの写真をサンプルとして入れてください。(サンプルなどの表記をお願いします)
ページ数
1ページ
希望イメージ
シンプル 複雑
単色 カラフル
暗い 明るい
日常 高級
遊び心 厳粛
未来的 伝統的
女性的 男性的
希望する色
青系、水色系、明るい色味
納品ファイル
• 高解像度JPG (.jpg)
• イラストレーター形式 (.ai)
• フォトショップ形式 (.psd)
• PNG形式 (.png)
補足説明
上記のいずれか1つ。アウトラインありとなしの2つ。

クライアントのイメージ通りでした。

たくさんのご提案ありがとうございました。
次回もぜひ、よろしくお願い致します。

```html
<!DOCTYPE html>
<html lang="ja">
<head>
<meta charset="utf-8">
<title>ミナモ工業株式会社</title>
<link href="https://fonts.googleapis.com/css2?family=Montserrat:wght@600;700;800&family=Noto+Sans+JP:wght@400;500;700&display=swap" rel="stylesheet">
<style>
:root{
  --blue:#1b9ae0;
  --blue-dark:#0f7fc4;
  --sky:#e5f4fc;
  --sky-2:#cfeaf8;
  --red:#e2231a;
  --green:#2fb14a;
  --ink:#333;
  --muted:#777;
  --line:#e2e2e2;
  --white:#fff;
}
*{box-sizing:border-box;margin:0;padding:0}
html,body{width:1200px;height:2980px;overflow:hidden}
body{font-family:"Noto Sans JP",sans-serif;color:var(--ink);background:var(--white);position:relative;font-size:14px}
.en{font-family:"Montserrat",sans-serif}
a{color:inherit;text-decoration:none}

/* header */
.site-header{position:absolute;top:0;left:0;width:1200px;height:80px;z-index:5;background:rgba(255,255,255,.92)}
.brand{position:absolute;left:20px;top:14px;display:flex;align-items:center;gap:8px}
.brand-mark{width:14px;height:14px;border-radius:50%;background:var(--blue)}
.brand-name{font-family:"Montserrat",sans-serif;font-weight:800;font-size:26px;color:var(--blue);letter-spacing:1px}
.global-nav{position:absolute;left:560px;top:48px;display:flex;gap:26px;font-size:13px;font-weight:500}
.search{position:absolute;left:800px;top:14px;width:250px;height:26px;border:1px solid var(--line);border-radius:3px;font-size:11px;color:#aaa;padding:5px 10px}
.search svg{position:absolute;right:8px;top:6px}
.header-contact{position:absolute;right:0;top:0;width:140px;height:80px;background:var(--blue);color:#fff;font-size:13px;font-weight:700;display:flex;align-items:center;justify-content:center;gap:6px}

/* hero */
.hero{position:absolute;top:0;left:0;width:1200px;height:770px;background:linear-gradient(100deg,#eef3f4 0%,#dfe8ea 40%,#f4efe9 70%,#e8ded2 100%)}
.hero-copy{position:absolute;left:200px;top:270px}
.hero-copy h1{font-size:24px;line-height:1.7;font-weight:700;color:var(--ink)}
.hero-copy h1 span{background:#fff;padding:2px 8px}
.hero-btn{display:inline-block;margin-top:24px;background:var(--blue);color:#fff;font-size:12px;padding:12px 34px;border-radius:24px}

/* section titles */
.sec-title{text-align:center}
.sec-title .en{font-size:34px;font-weight:800;color:var(--blue);letter-spacing:2px}
.sec-title .ja{font-size:14px;font-weight:500;margin-top:4px}
.pill-btn{display:block;margin:0 auto;width:240px;height:44px;line-height:44px;text-align:center;background:var(--blue);color:#fff;font-size:13px;font-weight:500;border-radius:22px}

/* products */
.products{position:absolute;top:770px;left:0;width:1200px;height:600px}
.products .sec-title{margin-top:48px}
.product-track{position:absolute;top:150px;left:180px;display:flex;gap:28px}
.product{width:190px;text-align:center;font-size:12px}
.product-img{width:190px;height:190px;border:1px solid var(--line);position:relative}
.product-tag{display:inline-block;margin:10px 0 6px;font-size:10px;color:#fff;padding:2px 14px}
.arrow{position:absolute;top:235px;width:34px;height:34px;border-radius:50%;background:var(--blue);display:flex;align-items:center;justify-content:center}
.dots{position:absolute;top:430px;left:0;width:1200px;display:flex;justify-content:center;gap:10px}
.dots i{width:9px;height:9px;border-radius:50%;background:#cde6f4}
.dots i.on{background:var(--blue)}
.products .pill-btn{position:absolute;top:470px;left:480px}

/* information */
.information{position:absolute;top:1370px;left:0;width:1200px;height:530px;background:var(--sky)}
.information .sec-title{margin-top:60px}
.news{position:absolute;top:180px;left:250px;width:700px;list-style:none}
.news li{display:flex;align-items:center;gap:18px;height:42px;border-bottom:1px solid var(--sky-2);font-size:12px}
.news time{width:80px;color:var(--muted)}
.news .cat{width:80px;text-align:center;color:#fff;font-size:10px;padding:3px 0}
.information .pill-btn{position:absolute;top:365px;left:480px}
.wave{position:absolute;left:0;width:1200px}

/* feature cards */
.features{position:absolute;top:1920px;left:180px;display:flex;gap:32px}
.feature{width:260px;height:580px;border:4px solid var(--blue);background:#fff;text-align:center}
.feature.shop{border-color:var(--red)}
.feature-img{width:252px;height:260px}
.feature h2{font-family:"Montserrat",sans-serif;font-size:30px;font-weight:800;color:var(--blue);margin-top:28px;letter-spacing:1px}
.feature.shop h2{color:var(--red)}
.feature h3{font-size:15px;font-weight:700;margin-top:2px}
.feature p{font-size:11px;line-height:1.8;color:var(--muted);margin:16px 28px 0;text-align:left}
.feature .more{display:block;margin:22px auto 0;width:150px;height:32px;line-height:32px;background:var(--blue);color:#fff;font-size:11px;border-radius:16px}
.feature.shop .more{background:var(--red)}

/* contact */
.contact{position:absolute;top:2560px;left:0;width:1200px;height:200px;background:var(--sky)}
.contact-head{position:absolute;left:140px;top:50px}
.contact-head .en{font-size:28px;font-weight:800;color:var(--blue)}
.contact-head .ja{font-size:14px;font-weight:700}
.contact-head p{font-size:11px;color:var(--muted);margin-top:8px;line-height:1.7}
.contact-btn{position:absolute;top:70px;width:200px;height:60px;border-radius:30px;color:#fff;font-size:14px;font-weight:700;display:flex;align-items:center;justify-content:center;gap:8px}
.contact-btn.faq{left:480px;background:var(--green)}
.contact-btn.mail{left:720px;background:var(--blue)}

/* footer */
.site-footer{position:absolute;top:2760px;left:0;width:1200px;height:220px;background:#fff}
.foot-links{position:absolute;top:30px;left:200px;display:flex;gap:80px;list-style:none}
.foot-links ul{list-style:none}
.foot-links li{font-size:11px;line-height:2.1}
.foot-links li::before{content:"›";color:var(--blue);margin-right:6px}
.foot-company{position:absolute;top:30px;left:720px;font-size:11px;line-height:1.8}
.foot-company .brand-name{font-size:22px}
.foot-company strong{display:block;font-size:12px;margin-top:4px}
.copyright{position:absolute;bottom:0;left:0;width:1200px;height:36px;background:var(--blue);color:#fff;font-size:10px;text-align:center;line-height:36px}
.pagetop{position:absolute;right:30px;top:2690px;width:48px;height:48px;border-radius:50%;background:var(--blue);display:flex;align-items:center;justify-content:center;z-index:4}
</style>
</head>
<body>

<section class="hero">
  <div role="img" aria-label="キッチンで野菜を洗う女性の写真" style="position:absolute;inset:0;background:linear-gradient(100deg,#edf2f3 0%,#dde7ea 45%,#e9e1d6 75%,#d9ccbc 100%)"></div>
  <div class="hero-copy">
    <h1><span>ミナモ工業の商品が</span><br><span>日々の生活に新提案</span></h1>
    <a class="hero-btn" href="#">ミナモ工業について</a>
  </div>
</section>

<header class="site-header">
  <div class="brand"><span class="brand-mark"></span><span class="brand-name">MINAMO</span></div>
  <nav class="global-nav">
    <a href="#">ミナモ工業とは</a><a href="#">商品一覧</a><a href="#">卸販売</a><a href="#">会社概要</a><a href="#">採用情報</a>
  </nav>
  <div class="search">Search
    <svg width="12" height="12" viewBox="0 0 12 12"><circle cx="5" cy="5" r="4" fill="none" stroke="#999" stroke-width="1.4"/><line x1="8" y1="8" x2="11" y2="11" stroke="#999" stroke-width="1.4"/></svg>
  </div>
  <a class="header-contact" href="#">
    <svg width="16" height="12" viewBox="0 0 16 12"><rect x="1" y="1" width="14" height="10" fill="none" stroke="#fff" stroke-width="1.4"/><path d="M1 1l7 6 7-6" fill="none" stroke="#fff" stroke-width="1.4"/></svg>お問い合わせ</a>
</header>

<section class="products">
  <div class="sec-title"><div class="en">PRODUCTS</div><div class="ja">商品紹介</div></div>
  <div class="arrow" style="left:120px"><svg width="12" height="12" viewBox="0 0 12 12"><path d="M8 1L3 6l5 5" fill="none" stroke="#fff" stroke-width="2"/></svg></div>
  <div class="product-track">
    <div class="product"><div class="product-img" role="img" aria-label="カラフルな歯間ブラシの商品写真" style="background:linear-gradient(135deg,#f4fbff,#d8f0e6 50%,#f9e0ec)"></div><span class="product-tag" style="background:var(--blue)">ケア用品</span><div>歯間ブラシ カラーセット</div></div>
    <div class="product"><div class="product-img" role="img" aria-label="ピンクのキッチンツールの商品写真" style="background:linear-gradient(135deg,#fff,#f8d9e3)"></div><span class="product-tag" style="background:var(--red)">キッチン用品</span><div>パッとはさむ 便利クリップ</div></div>
    <div class="product"><div class="product-img" role="img" aria-label="収納ボックスの商品写真" style="background:linear-gradient(135deg,#f3f3f3,#4d5a57)"></div><span class="product-tag" style="background:var(--blue)">収納用品</span><div>スタックコンテナ 大</div></div>
    <div class="product"><div class="product-img" role="img" aria-label="モップの商品写真" style="background:linear-gradient(160deg,#dbe9f3,#b9d3e6 60%,#eef4f8)"></div><span class="product-tag" style="background:var(--blue)">掃除用品</span><div>フロアモップ</div></div>
  </div>
  <div class="arrow" style="left:1046px"><svg width="12" height="12" viewBox="0 0 12 12"><path d="M4 1l5 5-5 5" fill="none" stroke="#fff" stroke-width="2"/></svg></div>
  <div class="dots"><i class="on"></i><i></i><i></i></div>
  <a class="pill-btn" href="#">商品一覧はこちら</a>
</section>

<svg class="wave" style="top:1320px" width="1200" height="52" viewBox="0 0 1200 52" preserveAspectRatio="none"><path d="M0 30 C300 0 500 60 800 30 S1100 10 1200 25 V52 H0Z" fill="#e5f4fc"/></svg>
<section class="information">
  <div class="sec-title"><div class="en">INFORMATION</div><div class="ja">お知らせ</div></div>
  <ul class="news">
    <li><time>2023.03.28</time><span class="cat" style="background:var(--blue)">お知らせ</span><span>新商品の取り扱いを開始しました。詳しくは商品ページをご覧ください</span></li>
    <li><time>2023.03.18</time><span class="cat" style="background:var(--red)">重要</span><span>ゴールデンウィーク期間中の営業日と発送についてのご案内です</span></li>
    <li><time>2023.03.16</time><span class="cat" style="background:var(--blue)">お知らせ</span><span>公式ウェブサイトをリニューアルしました。今後ともよろしくお願いします</span></li>
  </ul>
  <a class="pill-btn" href="#">お知らせ一覧はこちら</a>
</section>
<svg class="wave" style="top:1898px" width="1200" height="40" viewBox="0 0 1200 40" preserveAspectRatio="none"><path d="M0 0 H1200 V10 C1000 40 700 0 400 24 S100 20 0 12Z" fill="#e5f4fc"/></svg>

<div class="features">
  <article class="feature">
    <div class="feature-img" role="img" aria-label="会社の社屋の写真" style="background:linear-gradient(180deg,#cfe6f6,#e9eef1 55%,#9aa3a8)"></div>
    <h2>ABOUT US</h2><h3>会社案内</h3>
    <p>私たちは暮らしを便利にする日用品を企画・製造しています。会社の歩みや想いをご紹介します。</p>
    <a class="more" href="#">詳細はこちら</a>
  </article>
  <article class="feature">
    <div class="feature-img" role="img" aria-label="商品カタログの表紙写真" style="background:linear-gradient(135deg,#f2d24a,#e86a8a 50%,#6cc0e6)"></div>
    <h2>CATALOG</h2><h3>総合カタログ</h3>
    <p>取り扱い商品を一冊にまとめた総合カタログです。最新版をダウンロードしてご覧いただけます。</p>
    <a class="more" href="#">詳細はこちら</a>
  </article>
  <article class="feature shop">
    <div class="feature-img" role="img" aria-label="スマートフォンで買い物をするイメージ" style="background:linear-gradient(180deg,#fbe3e1,#f4a7a1 60%,#fde9e8)"></div>
    <h2>ONLINE SHOP</h2><h3>公式ウェブショップ</h3>
    <p>ミナモ工業の商品は公式ウェブショップからご購入いただけます。お得な情報も掲載中です。</p>
    <a class="more" href="#">購入はこちら</a>
  </article>
</div>

<section class="contact">
  <div class="contact-head">
    <div class="en">CONTACT</div><div class="ja">お問い合わせ</div>
    <p>商品や卸販売に関するご質問は<br>お気軽にお問い合わせください。</p>
  </div>
  <a class="contact-btn faq" href="#"><svg width="18" height="18" viewBox="0 0 18 18"><circle cx="9" cy="9" r="8" fill="none" stroke="#fff" stroke-width="1.6"/><text x="9" y="13" text-anchor="middle" font-size="11" font-weight="700" fill="#fff" font-family="sans-serif">?</text></svg>よくあるご質問</a>
  <a class="contact-btn mail" href="#"><svg width="18" height="13" viewBox="0 0 18 13"><rect x="1" y="1" width="16" height="11" fill="none" stroke="#fff" stroke-width="1.6"/><path d="M1 1l8 6 8-6" fill="none" stroke="#fff" stroke-width="1.6"/></svg>お問い合わせ</a>
</section>

<a class="pagetop" href="#"><svg width="16" height="10" viewBox="0 0 16 10"><path d="M1 9l7-7 7 7" fill="none" stroke="#fff" stroke-width="2"/></svg></a>

<footer class="site-footer">
  <div class="foot-links">
    <ul><li>HOME</li><li>ミナモ工業とは</li><li>商品一覧</li><li>卸販売</li><li>採用情報</li><li>会社概要</li></ul>
    <ul><li>お知らせ</li><li>よくあるご質問</li><li>カタログ</li><li>個人情報保護方針</li><li>サイトマップ</li></ul>
  </div>
  <div class="foot-company">
    <span class="brand-name">MINAMO</span>
    <strong>ミナモ工業株式会社</strong>
    〒000-0000<br>みなと県あおば市しらかわ町1-2-3<br>TEL：000-000-0000<br>FAX：000-000-0001
  </div>
  <div class="copyright">Copyright © MINAMO INDUSTRY Co.,Ltd. All Rights Reserved.</div>
</footer>

</body>
</html>
```